Corvallin Property Solutions need a business card design

Hello guys. We would need a business card design asap please.
We are a start up property investment business based in London UK specialised in buying, selling, managing and letting properties and helping distressed property owners.
The name of our Business is Corvallin, the logo symbolises the four fundamental elements of the world (earth, air, fire and water) and so it stands for strength, stability, longevity.
We would like the business card to communicate professionalism and reliability. Many many thanks indeed for your work.

Details:

1.) Marisol Dunkley
Property Investor
Mobile: +44(0)7700362517
Email: marisol.corvallin@quilbrook.example

2.) Tomas Brindle
Property Investor
Mobile: +44(0)7700845926
Email: tomas.corvallin@quilbrook.example

Industry/Entity Type

Investment

```html
<!DOCTYPE html>
<html lang="en">
<head>
<meta charset="utf-8">
<title>Corvallin Property Solutions — Business Card</title>
<link rel="stylesheet" href="https://fonts.googleapis.com/css2?family=Montserrat:wght@300;400;700;800;900&display=swap">
<style>
  :root {
    --backdrop: #7b7b7b;
    --card-top: #000000;
    --card-bottom: #121212;
    --ink: #ffffff;
    --fire-red: #e61e2c;
    --earth-green: #00882f;
    --water-blue: #005ccf;
  }
  * { box-sizing: border-box; margin: 0; padding: 0; }
  html, body {
    width: 1038px;
    height: 1200px;
    overflow: hidden;
    background: var(--backdrop);
    font-family: "Montserrat", sans-serif;
    color: var(--ink);
  }
  .card {
    position: absolute;
    left: 13px;
    width: 1012px;
    height: 577px;
    background: linear-gradient(180deg, var(--card-top) 0%, var(--card-bottom) 55%, var(--card-top) 100%);
    box-shadow: 0 3px 8px rgba(0, 0, 0, 0.45);
    overflow: hidden;
  }
  .card--front { top: 13px; }
  .card--back { top: 607px; }
  .bands {
    position: absolute;
    inset: 0;
    width: 100%;
    height: 100%;
  }
  .band--red { fill: var(--fire-red); }
  .band--green { fill: var(--earth-green); }
  .band--blue { fill: var(--water-blue); }

  .wordmark {
    position: absolute;
    text-align: center;
    font-weight: 700;
    color: var(--ink);
    text-transform: uppercase;
  }
  .wordmark__name { display: block; letter-spacing: 0.5px; }
  .wordmark__tagline { display: block; }

  .card--front .wordmark {
    left: 0; right: 0;
    top: 362px;
  }
  .card--front .wordmark__name { font-size: 46px; line-height: 56px; }
  .card--front .wordmark__tagline { font-size: 20px; line-height: 28px; margin-top: 12px; margin-left: -14px; }

  .front-email {
    position: absolute;
    left: 0; right: 0;
    top: 540px;
    text-align: center;
    font-size: 19px;
    font-weight: 400;
    text-transform: uppercase;
  }

  .card--back .wordmark {
    left: 52px;
    width 260px;
    width: 260px;
    top: 230px;
  }
  .card--back .wordmark__name { font-size: 26px; line-height: 32px; }
  .card--back .wordmark__tagline { font-size: 13px; line-height: 18px; margin-top: 4px; }

  .person {
    position: absolute;
    left: 300px;
    width: 540px;
    top: 212px;
    text-align: center;
    text-transform: uppercase;
  }
  .person__name { font-size: 42px; font-weight: 900; line-height: 50px; letter-spacing: 0.5px; }
  .person__role { font-size: 30px; font-weight: 300; line-height: 36px; margin-top: 2px; }

  .contacts {
    position: absolute;
    right: 72px;
    top: 426px;
    list-style: none;
    text-align: right;
    font-size: 29px;
    font-weight: 400;
    line-height: 40px;
    text-transform: uppercase;
  }
  .contacts li { display: flex; align-items: center; justify-content: flex-end; gap: 10px; }
  .contacts .icon { fill: var(--ink); }
</style>
</head>
<body>

  <section class="card card--front" aria-label="Card front">
    <svg class="bands" viewBox="0 0 1050 599" preserveAspectRatio="none" aria-hidden="true">
      <polygon class="band--red" points="429,0 543,0 429,199"/>
      <polygon class="band--green" points="0,199 429,199 366,313 0,313"/>
      <polygon class="band--blue" points="621,199 1050,199 1050,313 683,313"/>
    </svg>
    <div class="wordmark">
      <span class="wordmark__name">Corvallin</span>
      <span class="wordmark__tagline">Property Solutions</span>
    </div>
    <p class="front-email">marisol.corvallin@quilbrook.example</p>
  </section>

  <section class="card card--back" aria-label="Card back">
    <svg class="bands" viewBox="0 0 1050 599" preserveAspectRatio="none" aria-hidden="true">
      <polygon class="band--red" points="608,0 720,0 608,196"/>
      <polygon class="band--green" points="0,334 528,334 463,448 0,448"/>
      <polygon class="band--blue" points="908,298 1050,298 1050,412 973,412"/>
    </svg>
    <div class="wordmark">
      <span class="wordmark__name">Corvallin</span>
      <span class="wordmark__tagline">Property Solutions</span>
    </div>
    <div class="person">
      <h1 class="person__name">Marisol Dunkley</h1>
      <p class="person__role">Property Investor</p>
    </div>
    <ul class="contacts">
      <li>
        <svg class="icon" width="20" height="20" viewBox="0 0 24 24" aria-hidden="true">
          <path d="M6.6 10.8c1.4 2.8 3.8 5.1 6.6 6.6l2.2-2.2c.3-.3.7-.4 1-.2 1.1.4 2.3.6 3.6.6.6 0 1 .4 1 1V20c0 .6-.4 1-1 1C10.6 21 3 13.4 3 4c0-.6.4-1 1-1h3.5c.6 0 1 .4 1 1 0 1.3.2 2.5.6 3.6.1.3 0 .7-.2 1l-2.3 2.2z"/>
        </svg>
        <span>+44(0)7700362517</span>
      </li>
      <li>
        <svg class="icon" width="30" height="22" viewBox="0 0 30 22" aria-hidden="true">
          <path d="M0 0h30v22H0z M2 3v16l8-8z M28 3l-8 8 8 8z M3 2l12 11L27 2z M11 12l-8 8h24l-8-8-4 3.5z" fill-rule="evenodd"/>
        </svg>
        <span>marisol.corvallin@quilbrook.example</span>
      </li>
    </ul>
  </section>

</body>
</html>
```